Decorative concrete business needs new business cards

Our company attracts homeowners and business with disposable cash. We are a artistic decorative coatings company that will transform your driveway, patio, floors or counter tops into a work of art. We also engrave logos and designs right into the concrete! We are upscale and very professional company. I am open for rearranging our logo on the business card and also to different color patterns. We like the blue and black as in BrushNest's logo. We also like blue and orange/yellow.

Target Market(s)

Adults 30-70

Industry/Entity Type

Concrete

Contact Information for Business Card

Simple: Name, phone, email, website and social media icons

Font styles to use
Serif

Colors

Designer to choose colors to be used in the design.

Requirements
Must have
• Must present a professional upscale appearance. I have attached before and after photos that show you what our industry does. Maybe I will have before and after photo on back of card.
Nice to have
• Artistic, but bold. Nothing whimsical or cute.
Should not have
• Should not have cartoon or childlike appearance.

```html
<!DOCTYPE html>
<html lang="en">
<head>
<meta charset="utf-8">
<title>Stonevale Coatings – Business Card</title>
<link href="https://fonts.googleapis.com/css2?family=Cinzel:wght@400;700&family=Open+Sans:wght@400&display=swap" rel="stylesheet">
<style>
  :root {
    --backdrop: #eceef0;
    --card-white: #fbfbfb;
    --brand-blue: #2389bf;
    --pattern-blue: #2a8fc4;
    --ink: #1f1f1f;
    --on-blue: #ffffff;
  }
  * { box-sizing: border-box; margin: 0; padding: 0; }
  html, body { width: 1200px; height: 900px; overflow: hidden; }
  body { background: var(--backdrop); position: relative; font-family: "Open Sans", sans-serif; }

  .card {
    position: absolute;
    width: 556px; height: 342px;
    border-radius: 40px;
    overflow: hidden;
    background: var(--card-white);
    box-shadow: 0 6px 18px rgba(0,0,0,0.12);
    display: flex;
  }
  .card--front { left: 238px; top: 62px; }
  .card--back  { left: 460px; top: 520px; }

  .card__white { width: 266px; height: 100%; display: flex; align-items: center; justify-content: center; }
  .card__blue  { flex: 1; height: 100%; background: var(--brand-blue); }

  .brand { display: flex; align-items: center; gap: 10px; }
  .brand__mark { width: 40px; height: 40px; background: var(--brand-blue); }
  .brand__name {
    font-family: "Cinzel", serif; font-weight: 700;
    color: var(--brand-blue); font-size: 19px; line-height: 1.15; letter-spacing: 0.5px;
  }

  .contact { padding: 84px 0 0 16px; color: var(--on-blue); }
  .contact__name { font-family: "Cinzel", serif; font-weight: 700; font-size: 25px; letter-spacing: 0.5px; line-height: 1; }
  .contact__role { font-family: "Cinzel", serif; font-size: 15px; margin-top: 6px; letter-spacing: 0.4px; }
  .contact__list { list-style: none; margin-top: 14px; font-size: 15px; }
  .contact__list li { display: flex; align-items: center; gap: 9px; height: 23px; }
  .contact__list svg { width: 13px; height: 13px; fill: var(--on-blue); flex: none; }
  .social { display: flex; gap: 17px; margin-top: 24px; }
  .social span { width: 18px; height: 18px; border-radius: 3px; background: var(--on-blue); }

  .card__pattern { flex: 1; height: 100%; background: linear-gradient(135deg, var(--brand-blue), var(--pattern-blue)); }
</style>
</head>
<body>
  <section class="card card--front">
    <div class="card__white">
      <div class="brand">
        <span class="brand__mark"></span>
        <span class="brand__name">STONEVALE<br>COATINGS</span>
      </div>
    </div>
    <div class="card__blue">
      <div class="contact">
        <h1 class="contact__name">DANIEL HARTWELL</h1>
        <p class="contact__role">General Manager</p>
        <ul class="contact__list">
          <li><svg viewBox="0 0 16 16"><path d="M3 2h3l1.5 3.5-2 1.2a8 8 0 0 0 3.8 3.8l1.2-2L14 10v3a1 1 0 0 1-1 1A12 12 0 0 1 2 3a1 1 0 0 1 1-1z"/></svg>0400 512 377</li>
          <li><svg viewBox="0 0 16 16"><path d="M1 3h14v10H1z M2 4.2v.6l6 4 6-4v-.6z" fill-rule="evenodd"/></svg>hello@stonevale.com</li>
          <li><svg viewBox="0 0 16 16"><circle cx="8" cy="8" r="7"/></svg>www.stonevale.com</li>
        </ul>
        <div class="social" aria-hidden="true"><span></span><span></span><span></span><span></span></div>
      </div>
    </div>
  </section>

  <section class="card card--back">
    <div class="card__white">
      <div class="brand">
        <span class="brand__mark"></span>
        <span class="brand__name">STONEVALE<br>COATINGS</span>
      </div>
    </div>
    <div class="card__pattern" role="img" aria-label="Repeating faint brand-mark pattern on blue"></div>
  </section>
</body>
</html>
```